Design website home page for pathology consulting company

Starting a new consulting company with anatomic pathologists focused on expert diagnosis and second opinions on difficult pathology cases. In the near future we will be incorporating next generation diagnostics for rare diseases of childhood into the business. These include discovery and testing of DNA for mutations.

The company is formed around one of the best known pathologists in the world named Harold "Juniper" Tolvik. The name of the company is "JuniperLab"

We had a logo design by ArtfulHive - it is great. I will attach file as soon as I have it (contest ending today). Our company is medical, uses microscopes, DNA, probably will focus on childhood diseases but not solely on childhood diseases. we're not particularly conservative, but the customers we want to appeal to include older practicing pathologists as well as patients (sometimes parents) looking for second opinions.

Think a group of expert doctors diagnosing disease through the microscope and through DNA technology, ages ranging from 35-75 all trained by the best pathologist in the world - "Juniper"

We receive glass slides from diseases from patients all over the world from docs who need an expert to tell them what is the diagnosis. So "path to the diagnosis" is also part of the company marketing message.

We want the website design to describe our company but be very simple to find what one is looking for as we will use it as the launch page to:
1) order services
2) check results/reports
3) set up new account
4) speak with one of the pathologists
5) see our test menu
6) access our educational material/webinars
Updates

Update - looking for home page design and then finalists will ask for second page design to keep with theme - ok?

Reason: realized this project isn't web design but web home page design - thanks

Reason: Holidays for some in next two weeks

Reason: Hot discussion among collaborators for a few of the submissions. Will provide detail individually this weekend. Thanks so much for all the submissions!

Target Market(s)

Referring pathologists, physicians who want second opinions on pathology disease diagnosis, patients who have had biopsies (either patients themselves or parents of patients), generally high education level

Industry/Entity Type

Marketing

Requirements
Must have
• JuniperLab
Next Generation Pathology Consultants

```html
<!DOCTYPE html>
<html lang="en">
<head>
<meta charset="utf-8">
<title>JuniperLab — Next Generation Pathology Consultants</title>
<link rel="stylesheet" href="https://fonts.googleapis.com/css2?family=Open+Sans:wght@300;400;600&display=swap">
<style>
  :root {
    --brand-blue: #2a62a6;
    --brand-blue-dark: #1f4f8c;
    --nav-divider: #5d87bd;
    --ink: #333333;
    --heading-grey: #555555;
    --body-grey: #7a7a7a;
    --muted: #9a9a9a;
    --rule: #e2e2e2;
    --page: #ffffff;
    --field: #f4f4f4;
  }
  * { box-sizing: border-box; margin: 0; padding: 0; }
  html, body { width: 1200px; height: 1200px; overflow: hidden; background: var(--page); }
  body { font-family: "Open Sans", Arial, sans-serif; color: var(--ink); position: relative; }

  .site-header { position: absolute; left: 0; top: 0; width: 1200px; height: 184px; }
  .brand { position: absolute; left: 104px; top: 50px; display: flex; align-items: center; }
  .brand-mark { width: 96px; height: 86px; border-radius: 50%; background: var(--brand-blue); }
  .brand-text { margin-left: 28px; }
  .brand-name { font-size: 27px; font-weight: 400; color: var(--brand-blue); letter-spacing: 0.5px; line-height: 1; }
  .brand-tagline { font-size: 9.5px; color: var(--body-grey); margin-top: 4px; }

  .welcome { position: absolute; left: 677px; top: 89px; font-size: 11.5px; color: var(--ink); letter-spacing: 0.3px; }
  .account-links { position: absolute; left: 852px; top: 89px; font-size: 12px; color: var(--muted); display: flex; gap: 22px; }
  .utility-icons { position: absolute; left: 1008px; top: 85px; display: flex; gap: 11px; }
  .utility-icons svg { width: 21px; height: 21px; display: block; }

  .main-nav { position: absolute; left: 100px; top: 184px; width: 990px; height: 53px; background: var(--brand-blue); display: flex; }
  .main-nav a { color: #fff; text-decoration: none; font-size: 14.5px; font-weight: 400; display: flex; align-items: center; justify-content: center; border-right: 2px solid var(--nav-divider); height: 100%; }
  .main-nav a:last-child { border-right: none; }
  .nav-pointer { position: absolute; left: 148px; top: 184px; width: 0; height: 0; border-left: 8px solid transparent; border-right: 8px solid transparent; border-top: 7px solid var(--page); }

  .hero { position: absolute; left: 100px; top: 237px; width: 990px; height: 426px; overflow: hidden; }
  .hero-photo { position: absolute; inset: 0; background: linear-gradient(100deg, #dfe3e2 0%, #f2f3f2 30%, #e8ecec 55%, #f4f5f5 75%, #d7dcdc 100%); }
  .hero-copy { position: absolute; left: 600px; top: 146px; width: 380px; }
  .hero-title { font-size: 33px; font-weight: 400; color: var(--brand-blue); line-height: 39px; letter-spacing: 0.3px; }
  .hero-lead { margin-top: 32px; font-size: 11.5px; line-height: 15px; color: var(--brand-blue); }
  .hero-link { margin-top: 26px; display: flex; align-items: center; gap: 14px; font-size: 14.5px; color: var(--brand-blue); }
  .hero-dots { position: absolute; left: 480px; top: 400px; display: flex; gap: 4px; }
  .hero-dots span { width: 8px; height: 8px; border-radius: 50%; background: #3a3a3a; opacity: .55; }
  .hero-dots span:first-child { background: var(--brand-blue); opacity: 1; }

  .features { position: absolute; left: 0; top: 723px; width: 1200px; }
  .feature { position: absolute; width: 280px; text-align: center; }
  .feature-icon { width: 90px; height: 90px; margin: 0 auto; display: block; }
  .feature-title { margin-top: 36px; font-size: 25px; font-weight: 400; color: var(--heading-grey); }
  .feature-text { margin-top: 17px; font-size: 14.5px; line-height: 21px; color: var(--body-grey); font-weight: 300; }

  .section-rule { position: absolute; left: 183px; top: 999px; width: 836px; height: 1px; background: var(--rule); }

  .order-service { position: absolute; left: 183px; top: 1055px; }
  .order-service h2 { font-size: 28px; font-weight: 400; color: var(--ink); }
  .service-list { list-style: none; margin-top: 28px; }
  .service-list li { display: flex; align-items: center; height: 49px; font-size: 15.5px; font-weight: 300; color: var(--ink); }
  .service-list li svg { width: 21px; height: 21px; margin-right: 18px; flex: none; }
  .service-list li:first-child .service-label { border-bottom: 1px solid var(--rule); }
  .service-label { display: inline-block; width: 248px; padding: 13px 0 12px; }

  .order-form { position: absolute; left: 722px; top: 1095px; }
  .order-form-head { display: flex; align-items: center; gap: 22px; }
  .order-form-head h2 { font-size: 30px; font-weight: 400; color: var(--ink); }
  .field { margin-top: 34px; width: 264px; height: 40px; background: var(--field); border: 1px solid #e6e6e6; padding: 8px 23px; font-size: 11.5px; color: var(--heading-grey); }
</style>
</head>
<body>

<header class="site-header">
  <div class="brand">
    <div class="brand-mark" aria-hidden="true"></div>
    <div class="brand-text">
      <div class="brand-name">JuniperLab</div>
      <div class="brand-tagline">Next Generation Pathology Consultants</div>
    </div>
  </div>
  <div class="welcome">WELCOME MESSAGE!</div>
  <div class="account-links"><span>Sign Up</span><span>I</span><span>Login</span></div>
  <div class="utility-icons">
    <svg viewBox="0 0 21 21" aria-label="Phone"><circle cx="10.5" cy="10.5" r="10.5" fill="var(--brand-blue-dark)"/><path d="M7 5.5c.6-.3 1.1 0 1.4.6l.8 1.6c.2.5 0 1-.4 1.3l-.6.4c.5 1.2 1.4 2.2 2.6 2.8l.5-.6c.3-.4.9-.5 1.3-.3l1.6.8c.6.3.8.9.5 1.4l-.6 1c-.4.6-1.2.8-1.9.5C9.3 13.9 7.1 11.6 6 8.7c-.3-.7 0-1.5.5-1.9z" fill="#fff"/></svg>
    <svg viewBox="0 0 21 21" aria-label="Email"><circle cx="10.5" cy="10.5" r="10.5" fill="var(--brand-blue-dark)"/><rect x="5.5" y="7" width="10" height="7" rx="1" fill="#fff"/><path d="M5.8 7.5l4.7 3.5 4.7-3.5" stroke="var(--brand-blue-dark)" stroke-width="1" fill="none"/></svg>
    <svg viewBox="0 0 21 21" aria-label="Search"><circle cx="10.5" cy="10.5" r="10.5" fill="var(--brand-blue-dark)"/><circle cx="9.5" cy="9.5" r="3" stroke="#fff" stroke-width="1.5" fill="none"/><path d="M11.7 11.7l2.8 2.8" stroke="#fff" stroke-width="1.6" stroke-linecap="round"/></svg>
  </div>
</header>

<nav class="main-nav">
  <a href="#" style="width:108px">HOME</a>
  <a href="#" style="width:116px">SERVICES</a>
  <a href="#" style="width:178px">MEDICAL REPORTS</a>
  <a href="#" style="width:155px">OUR DOCTORS</a>
  <a href="#" style="width:117px">PATIENTS</a>
  <a href="#" style="width:96px">FAQ' s</a>
  <a href="#" style="width:91px">BLOG</a>
  <a href="#" style="width:129px">CONTACT</a>
</nav>
<div class="nav-pointer" aria-hidden="true"></div>

<section class="hero">
  <div class="hero-photo" role="img" aria-label="Photograph of laboratory scientists in white coats and safety glasses working at a microscope"></div>
  <div class="hero-copy">
    <h1 class="hero-title">VERITATIS EXPLICABO<br>DOLORES UT&nbsp; DICTA</h1>
    <p class="hero-lead">Lorem ipsum dolor amet rem eos illo omnis<br>aut aperiam ab ipsam ipsa odit aut aperiam<br>aut aspernatur veritatis unde unde sed enim</p>
    <div class="hero-link">Learn More
      <svg width="22" height="22" viewBox="0 0 22 22" aria-hidden="true"><circle cx="11" cy="11" r="9.8" stroke="var(--brand-blue)" stroke-width="1.5" fill="none"/><path d="M9.3 6.8l4.2 4.2-4.2 4.2" stroke="var(--brand-blue)" stroke-width="1.6" fill="none"/></svg>
    </div>
  </div>
  <div class="hero-dots" aria-hidden="true"><span></span><span></span><span></span><span></span><span></span></div>
</section>

<section class="features">
  <div class="feature" style="left:177px">
    <svg class="feature-icon" viewBox="0 0 90 90" aria-hidden="true"><circle cx="45" cy="45" r="43.5" stroke="var(--brand-blue)" stroke-width="2" fill="none"/><path d="M30 28h20l10 10v25H30z M50 28v10h10" stroke="var(--brand-blue)" stroke-width="2" fill="none" stroke-linejoin="round"/></svg>
    <h3 class="feature-title">Medical Reports</h3>
    <p class="feature-text">Dolores voluptatem dolorem beatiae<br>atione ratione dolores&nbsp; veritatis unde</p>
  </div>
  <div class="feature" style="left:460px">
    <svg class="feature-icon" viewBox="0 0 90 90" aria-hidden="true"><circle cx="45" cy="45" r="43.5" stroke="var(--brand-blue)" stroke-width="2" fill="none"/><path d="M28 28h24l10 10v25H28z M52 28v10h10" stroke="var(--brand-blue)" stroke-width="1.4" fill="none" stroke-linejoin="round"/><path d="M37 40h14M37 44h16M37 48h16M37 52h16M37 56h16" stroke="var(--brand-blue)" stroke-width="1"/></svg>
    <h3 class="feature-title">Test Menu</h3>
    <p class="feature-text">Dolores voluptatem dolorem beatiae<br>atione ratione dolores&nbsp; veritatis unde</p>
  </div>
  <div class="feature" style="left:745px">
    <svg class="feature-icon" viewBox="0 0 90 90" aria-hidden="true"><circle cx="45" cy="45" r="43.5" stroke="var(--brand-blue)" stroke-width="2" fill="none"/><path d="M28 28h24l10 10v25H28z M52 28v10h10" stroke="var(--brand-blue)" stroke-width="1.4" fill="none" stroke-linejoin="round"/><path d="M42 43l-4 4 4 4M48 43l4 4-4 4" stroke="var(--brand-blue)" stroke-width="1.2" fill="none"/></svg>
    <h3 class="feature-title">Webinars</h3>
    <p class="feature-text">Dolores voluptatem dolorem beatiae<br>atione ratione dolores&nbsp; veritatis unde</p>
  </div>
</section>

<div class="section-rule" aria-hidden="true"></div>

<section class="order-service">
  <h2>Order Service</h2>
  <ul class="service-list">
    <li><svg viewBox="0 0 21 21" aria-hidden="true"><circle cx="10.5" cy="10.5" r="9.5" stroke="var(--brand-blue)" stroke-width="1.4" fill="none"/><path d="M6.5 10.5h8" stroke="var(--brand-blue)" stroke-width="1.4"/></svg><span class="service-label">Fugit aut illo omnis explicabo ipsa</span></li>
    <li><svg viewBox="0 0 21 21" aria-hidden="true"><circle cx="10.5" cy="10.5" r="9.5" stroke="var(--brand-blue)" stroke-width="1.4" fill="none"/><path d="M6.5 10.5h8" stroke="var(--brand-blue)" stroke-width="1.4"/></svg><span class="service-label">Rem ipsam quai illo dolores</span></li>
  </ul>
</section>

<section class="order-form">
  <div class="order-form-head">
    <svg width="36" height="48" viewBox="0 0 36 48" aria-hidden="true"><path d="M8 1h16l10 10v30H8z M24 1v10h10" stroke="var(--brand-blue)" stroke-width="1.6" fill="#fff" stroke-linejoin="round"/><path d="M2 7h16l10 10v30H2z M18 7v10h10" stroke="var(--brand-blue)" stroke-width="1.6" fill="#fff" stroke-linejoin="round"/></svg>
    <h2>Order Form</h2>
  </div>
  <div class="field">full name</div>
</section>

</body>
</html>
```